Veltrano Energy Business Card Design

website: www.veltranoenergy.example
Project: Business Card Design for Veltrano Energy
Name: Dorian Kettle
Title: Founder / Operations Strategist
Visual Identity & Logo:
Logo File: VEL-Logo-FullGradient-Final.png (Attached).
Color Palette: The brand relies on a distinctive Cyan (Blue) to Lime Green gradient.
Background Preference: We want a Dark Mode aesthetic (Deep Matte Black, Charcoal, or Dark Slate) to make the neon gradient of the logo pop. This feels more "tech/industrial" than a standard white card.
Design Aesthetic (The "Ops" Vibe):
Concept: "Grid & Infrastructure." We are a solar rental company, focusing on logistics and access.
Typography: White, bold sans-serif text for contact info. High contrast against the dark background.
Accents: Use the Cyan or Lime Green from the logo for thin divider lines or edge painting.
Avoid: No orange/gold (clashes with logo). No cartoon leaves.
Layout Requirements:
Front: Large, centered logo. Maybe a subtle UV gloss spot varnish over the logo icon.
Back: Name, Title, Contact Info.
Texture: Matte finish cardstock with gloss elements.
sample mock up of information on card: https://brivomarkco-my.filehost.example/:i:/g/personal/dorian_kettle_veltranoenergy_example/AbCdEfGhIjKlMnOpQrStUvWxYz012345678?e=Xy12Ab
Logo: https://brivomarkco.filehost.example/:i:/s/VeltranoEnergy/ZyXwVuTsRqPoNmLkJiHgFeDcBa9876543210?e=Pq34Cd

```html
<!DOCTYPE html>
<html lang="en">
<head>
<meta charset="utf-8">
<title>Veltrano Energy – Business Card</title>
<link href="https://fonts.googleapis.com/css2?family=Montserrat:wght@400;500;600;700&display=swap" rel="stylesheet">
<style>
  :root {
    --stage: #3a3b3d;
    --card-light: #ffffff;
    --card-dark: #1f1f20;
    --cyan: #12a9dc;
    --teal: #1ec8c0;
    --lime: #9ed82a;
    --ink: #1c1c1c;
    --paper-text: #ffffff;
    --brand-gradient: linear-gradient(90deg, var(--cyan), var(--teal) 45%, var(--lime));
  }
  * { box-sizing: border-box; margin: 0; padding: 0; }
  html, body { width: 1200px; height: 1200px; overflow: hidden; }
  body {
    background: var(--stage);
    font-family: "Montserrat", sans-serif;
    position: relative;
  }
  .card {
    position: absolute;
    left: 180px;
    width: 840px;
    height: 480px;
    border-radius: 36px;
    overflow: hidden;
  }

  /* ---------- Contact side ---------- */
  .card--contact { top: 90px; background: var(--card-light); color: var(--ink); }
  .card--contact .edge-band {
    position: absolute; left: 0; right: 0; bottom: 0; height: 14px;
    background: var(--brand-gradient);
  }
  .brand {
    position: absolute; display: flex; align-items: center;
  }
  .brand__square {
    background: var(--cyan); border-radius: 4px;
  }
  .brand__name {
    font-weight: 500; color: var(--cyan); letter-spacing: 0.5px; white-space: nowrap;
  }
  .card--contact .brand { left: 190px; top: 62px; gap: 18px; }
  .card--contact .brand__square { width: 44px; height: 44px; }
  .card--contact .brand__name { font-size: 48px; }

  .rule-long {
    position: absolute; left: 350px; top: 190px; width: 440px; height: 2px;
    background: linear-gradient(90deg, var(--teal), var(--lime));
  }
  .rule-short {
    position: absolute; left: 58px; top: 262px; width: 290px; height: 2px;
    background: var(--cyan);
  }
  .holder { position: absolute; left: 58px; top: 172px; }
  .holder__name { font-size: 34px; font-weight: 700; color: var(--cyan); letter-spacing: 0.5px; }
  .holder__title { font-size: 15px; font-weight: 500; letter-spacing: 0.6px; margin-top: 2px; }

  .contacts { position: absolute; left: 58px; top: 282px; list-style: none; }
  .contacts li {
    display: flex; align-items: flex-start; gap: 14px;
    font-size: 19px; line-height: 24px; margin-bottom: 6px;
  }
  .contacts svg { width: 22px; height: 22px; flex: none; margin-top: 1px; }

  .offices { position: absolute; right: 60px; top: 168px; text-align: center; }
  .offices__label { font-size: 18px; font-weight: 500; margin-bottom: 8px; }
  .offices__flags { display: flex; gap: 10px; }
  .flag { width: 40px; height: 40px; border-radius: 50%; }
  .flag--us { background: linear-gradient(180deg, #d7263d 0 50%, #1f3b8f 50%); }
  .flag--uk { background: linear-gradient(135deg, #1f3b8f 0 45%, #ffffff 45% 55%, #d7263d 55%); }
  .flag--ca { background: linear-gradient(90deg, #d7263d 0 28%, #ffffff 28% 72%, #d7263d 72%); }

  .slogan {
    position: absolute; right: 60px; bottom: 42px;
    font-size: 21px; font-weight: 600; color: var(--cyan); letter-spacing: 0.4px;
  }

  /* ---------- Brand side ---------- */
  .card--brand {
    top: 630px; background: var(--card-dark);
    box-shadow: inset 0 0 0 3px var(--teal);
  }
  .card--brand .brand-lockup {
    position: absolute; left: 0; right: 0; top: 170px;
    display: flex; flex-direction: column; align-items: center;
  }
  .card--brand .brand { position: static; gap: 22px; }
  .card--brand .brand__square { width: 64px; height: 64px; }
  .card--brand .brand__name { font-size: 66px; color: var(--teal); }
  .tagline {
    margin-top: 16px; margin-left: 180px;
    font-size: 21px; font-weight: 500; color: var(--paper-text); letter-spacing: 0.5px;
  }
</style>
</head>
<body>

<section class="card card--contact" aria-label="Business card, contact side">
  <div class="brand">
    <span class="brand__square"></span>
    <span class="brand__name">Veltrano Energy</span>
  </div>

  <div class="rule-long"></div>

  <div class="holder">
    <h1 class="holder__name">DORIAN KETTLE</h1>
    <p class="holder__title">FOUNDER / OPERATIONS STRATEGIST</p>
  </div>
  <div class="rule-short"></div>

  <ul class="contacts">
    <li>
      <svg viewBox="0 0 24 24" aria-hidden="true"><path fill="#12a9dc" d="M6.6 10.8a15.1 15.1 0 0 0 6.6 6.6l2.2-2.2c.3-.3.7-.4 1-.2 1.1.4 2.3.6 3.6.6.6 0 1 .4 1 1V20c0 .6-.4 1-1 1A17 17 0 0 1 3 4c0-.6.4-1 1-1h3.5c.6 0 1 .4 1 1 0 1.3.2 2.5.6 3.6.1.3 0 .7-.2 1z"/></svg>
      <span>407.555.0142</span>
    </li>
    <li>
      <svg viewBox="0 0 24 24" aria-hidden="true"><g fill="none" stroke="#12a9dc" stroke-width="1.8"><circle cx="12" cy="12" r="9"/><ellipse cx="12" cy="12" rx="4" ry="9"/><path d="M3 12h18M4.5 7.5h15M4.5 16.5h15"/></g></svg>
      <span>www.veltranoenergy.example</span>
    </li>
    <li>
      <svg viewBox="0 0 24 24" aria-hidden="true"><path fill="#12a9dc" d="M12 2a7 7 0 0 0-7 7c0 5.2 7 13 7 13s7-7.8 7-13a7 7 0 0 0-7-7zm0 9.5A2.5 2.5 0 1 1 12 6.5a2.5 2.5 0 0 1 0 5z"/></svg>
      <span>Veltrano Energy<br>1450 Marrow Creek Lane Orlando,<br>FL 32800</span>
    </li>
  </ul>

  <div class="offices">
    <p class="offices__label">Offices:</p>
    <div class="offices__flags">
      <span class="flag flag--us" role="img" aria-label="United States flag"></span>
      <span class="flag flag--uk" role="img" aria-label="United Kingdom flag"></span>
      <span class="flag flag--ca" role="img" aria-label="Canada flag"></span>
    </div>
  </div>

  <p class="slogan">No debt, no liens, no maintenance, just savings.</p>
  <div class="edge-band"></div>
</section>

<section class="card card--brand" aria-label="Business card, brand side">
  <div class="brand-lockup">
    <div class="brand">
      <span class="brand__square"></span>
      <span class="brand__name">Veltrano Energy</span>
    </div>
    <p class="tagline">Rent Solar. Generate Power. Save Smarter</p>
  </div>
</section>

</body>
</html>
```